Flyer for the Harvest Lantern Gathering 2018

Design a flyer for our annual conference with basic information about the conference: conference logo and year,

Location:
Tolvane Community Center (Downtown Portland)
482 Wexmoor Street, Portland, ME 04107,

Date:
August 24th, 25th and 26th, 2018
Start time 6:00PM

I would like the following three words added to the flyer. These words describe the vision of the conference:
Prophetic, Worship, Prayer

```html
<!DOCTYPE html>
<html lang="en">
<head>
<meta charset="utf-8">
<title>Harvest Lantern Gathering 2018 Flyer</title>
<link rel="stylesheet" href="https://fonts.googleapis.com/css2?family=Bebas+Neue&family=Montserrat:wght@600;700;800;900&display=swap">
<style>
  :root {
    --backdrop: #d4d4d4;
    --ink: #060606;
    --gold: #e6a60c;
    --orange: #e06008;
    --white: #ffffff;
    --flame-hot: #ffd24a;
    --flame-mid: #f08a12;
    --flame-deep: #a8300a;
    --band: rgba(214, 160, 20, 0.82);
  }
  html, body {
    margin: 0;
    width: 933px;
    height: 1200px;
    overflow: hidden;
    background: var(--backdrop);
  }
  .flyer {
    position: absolute;
    left: 42px;
    top: 0;
    width: 849px;
    height: 1200px;
    background: var(--ink);
    overflow: hidden;
    font-family: "Montserrat", sans-serif;
  }
  .flames {
    position: absolute;
    inset: 0;
    background:
      radial-gradient(ellipse 120px 380px at 40px 520px, rgba(240,138,18,0.75), transparent 70%),
      radial-gradient(ellipse 190px 300px at 110px 940px, rgba(255,190,60,0.85), transparent 72%),
      radial-gradient(ellipse 260px 220px at 200px 1080px, rgba(240,138,18,0.9), transparent 70%),
      radial-gradient(ellipse 110px 360px at 810px 620px, rgba(224,96,8,0.7), transparent 70%),
      radial-gradient(ellipse 170px 330px at 760px 960px, rgba(255,190,60,0.85), transparent 72%),
      radial-gradient(ellipse 260px 200px at 650px 1090px, rgba(240,138,18,0.85), transparent 70%),
      radial-gradient(ellipse 90px 260px at 20px 260px, rgba(168,48,10,0.6), transparent 70%);
  }
  .mark {
    position: absolute;
    left: 330px;
    top: 35px;
    width: 190px;
    height: 190px;
    box-sizing: border-box;
    border: 4px solid var(--gold);
    border-radius: 50%;
  }
  .brand-name {
    position: absolute;
    left: 0;
    right: 0;
    top: 232px;
    text-align: center;
    color: var(--white);
    font-weight: 700;
    font-size: 44px;
    letter-spacing: 3px;
    line-height: 1;
  }
  .vision-word {
    position: absolute;
    left: 94px;
    width: 658px;
    margin: 0;
    text-align: center;
    line-height: 1;
    font-weight: 800;
  }
  .vision-word--prophetic {
    top: 304px;
    color: var(--gold);
    font-size: 92px;
    letter-spacing: 5px;
  }
  .vision-word--worship {
    top: 387px;
    height: 129px;
    background: var(--orange);
    color: var(--white);
    font-size: 124px;
    font-weight: 900;
    line-height: 129px;
    letter-spacing: -2px;
  }
  .vision-word--prayer {
    top: 518px;
    color: var(--gold);
    font-size: 152px;
    font-weight: 900;
    letter-spacing: 1px;
  }
  .event-line {
    position: absolute;
    left: 0;
    right: 0;
    margin: 0;
    text-align: center;
    font-family: "Bebas Neue", sans-serif;
    font-weight: 400;
    line-height: 1;
    color: var(--white);
  }
  .event-name--first { top: 664px; font-size: 72px; color: var(--orange); }
  .event-name--second { top: 736px; font-size: 78px; }
  .event-days { top: 838px; font-size: 68px; }
  .event-month { top: 916px; font-size: 50px; color: var(--gold); letter-spacing: 3px; }
  .event-time { top: 979px; font-size: 62px; }
  .event-time__hour { font-size: 86px; color: var(--gold); vertical-align: -3px; }
  .venue {
    position: absolute;
    left: 0;
    right: 0;
    top: 1084px;
    height: 116px;
    background: var(--band);
    color: var(--white);
    font-weight: 700;
    font-size: 20px;
    line-height: 30px;
    text-align: center;
    padding-top: 26px;
    box-sizing: border-box;
  }
</style>
</head>
<body>
  <main class="flyer">
    <div class="flames" role="img" aria-label="Photograph of orange flames rising along both sides of the flyer"></div>

    <div class="mark"></div>
    <div class="brand-name">HARVESTCON</div>

    <h1 class="vision-word vision-word--prophetic">PROPHETIC</h1>
    <p class="vision-word vision-word--worship">WORSHIP</p>
    <p class="vision-word vision-word--prayer">PRAYER</p>

    <p class="event-line event-name--first">HARVEST LANTERN</p>
    <p class="event-line event-name--second">GATHERING 2018</p>
    <p class="event-line event-days">24TH, 25TH &amp; 26TH</p>
    <p class="event-line event-month">AUGUST 2018</p>
    <p class="event-line event-time">START AT <span class="event-time__hour">6PM</span></p>

    <footer class="venue">
      Tolvane Community Center (Downtown Portland)&nbsp; 482 Wexmoor Street,<br>
      Portland, ME 04107,
    </footer>
  </main>
</body>
</html>
```